Book cover for my book "Gentle Uncoupling"

Simple graphic with the title "Gentle Uncoupling" for a book I am self publishing. This book teaches people how to divorce with kindness and compassion without compromising their legal rights and getting what is fair. I am a lawyer telling them everything on how to hire a lawyer, what process to choose, how to build a support system, how to keep the kids out of it. It should exude authority, but also kindness and compassion. It's real legal information but from a lens that doesn't give a bunch of money to lawyers to burn down your family.

Target Market(s)

People seeking to divorce but don't want to spend a bunch of money or destroy their spouse

Industry/Entity Type

Legal

Requirements
Must have
• Dignity
Nice to have
• Envision two people parting, moving away from each other but something that is altruistic popping up between them? I'm not artist. Keep in mind "couple" is generic so not gender specific.
Should not have
• Trite things like a handshake,

```html
<!DOCTYPE html>
<html lang="en">
<head>
<meta charset="utf-8">
<title>Gentle Uncoupling — Book Cover</title>
<link href="https://fonts.googleapis.com/css2?family=Marcellus&display=swap" rel="stylesheet">
<style>
  :root {
    --stage: #8a8a8a;
    --paper: #eeeeee;
    --paper-edge: #d8d8d8;
    --ink: #1f1f1f;
    --crimson: #7e1416;
    --spine: #8a0f0f;
    --figure-core: #bdbdbd;
    --figure-mid: #d4d4d4;
    --figure-line: #3a3a36;
  }
  * { box-sizing: border-box; margin: 0; padding: 0; }
  html, body {
    width: 1200px;
    height: 908px;
    overflow: hidden;
    background: var(--stage);
  }
  .stage {
    position: relative;
    width: 1200px;
    height: 908px;
  }
  .book {
    position: absolute;
    left: 300px;
    top: 44px;
    width: 600px;
    height: 820px;
    display: flex;
    box-shadow: 0 10px 30px rgba(0,0,0,0.25);
  }
  .book__spine {
    width: 34px;
    height: 100%;
    background: linear-gradient(90deg, #6e0b0b 0%, var(--spine) 45%, #700c0c 100%);
  }
  .cover {
    position: relative;
    flex: 1;
    height: 100%;
    background: linear-gradient(180deg, #f3f3f3 0%, var(--paper) 60%, var(--paper-edge) 100%);
    font-family: "Marcellus", "Optima", serif;
  }
  .cover__hinge {
    position: absolute;
    left: 12px;
    top: 0;
    bottom: 0;
    width: 2px;
    background: #e0e0e0;
  }
  .cover__title {
    position: absolute;
    top: 112px;
    left: 0;
    right: 0;
    text-align: center;
    line-height: 1;
    font-weight: 400;
  }
  .cover__title-main {
    display: block;
    font-size: 62px;
    color: var(--ink);
    letter-spacing: 1px;
  }
  .cover__title-accent {
    display: block;
    margin-top: 10px;
    font-size: 56px;
    color: var(--crimson);
    letter-spacing: 1px;
  }
  .cover__rule {
    position: absolute;
    top: 262px;
    left: 118px;
    width: 350px;
    height: 12px;
  }
  .cover__figures {
    position: absolute;
    top: 300px;
    left: 95px;
    width: 390px;
    height: 410px;
    background: radial-gradient(ellipse 55% 60% at 50% 50%, var(--figure-core) 0%, var(--figure-mid) 50%, var(--paper) 100%);
    border-radius: 8px;
  }
  .cover__imprint {
    position: absolute;
    left: 0;
    right: 0;
    top: 728px;
    display: flex;
    flex-direction: column;
    align-items: center;
    gap: 8px;
  }
  .cover__imprint-line {
    width: 300px;
    height: 1px;
    background: #9a9a9a;
  }
  .cover__imprint-row {
    display: flex;
    align-items: center;
    gap: 12px;
  }
  .cover__imprint-dot {
    width: 20px;
    height: 20px;
    border-radius: 50%;
    background: var(--crimson);
  }
  .cover__imprint-name {
    font-size: 26px;
    color: var(--crimson);
    letter-spacing: 1px;
    text-transform: uppercase;
  }
</style>
</head>
<body>
  <main class="stage">
    <div class="book">
      <div class="book__spine"></div>
      <section class="cover">
        <div class="cover__hinge"></div>

        <h1 class="cover__title">
          <span class="cover__title-main">GENTLE</span>
          <span class="cover__title-accent">UNCOUPLING</span>
        </h1>

        <svg class="cover__rule" viewBox="0 0 350 12" aria-hidden="true">
          <path d="M0 11 Q175 4 350 1 Q175 6 0 11 Z" fill="var(--crimson)"/>
        </svg>

        <div class="cover__figures" role="img"
             aria-label="Line illustration of two people standing back to back, turning away from each other"></div>

        <div class="cover__imprint">
          <span class="cover__imprint-line"></span>
          <div class="cover__imprint-row">
            <span class="cover__imprint-dot"></span>
            <span class="cover__imprint-name">The Kindly Counsel</span>
          </div>
          <span class="cover__imprint-line"></span>
        </div>
      </section>
    </div>
  </main>
</body>
</html>
```